2 Page Brochure - Commercial Roofing Company

We are looking for a double sided brochure, full color, for our commercial roofing company that tells customers a little bit about the company, what we do, and shows a few pictures.
The brochure would need to have our logo and color scheme that coordinates with that logo.
I have uploaded our logo, some ideas I had, and then the idea list also has our website on there if you'd like to take a look around there for some more ideas.
I have also uploaded some photos we'd like to use.
Page size should be 8.5" x 11".
Target Market(s)
Commercial Property Owners
Other font styles liked:
- Match logo font ideally so it's cohesive, but whatever looks best

```html
<!DOCTYPE html>
<html lang="en">
<head>
<meta charset="utf-8">
<title>K&amp;R Roofing Brochure</title>
<link href="https://fonts.googleapis.com/css2?family=Montserrat:wght@500;600;700;800;900&family=Poppins:wght@400;500;600&display=swap" rel="stylesheet">
<style>
:root{
  --bg:#ebebeb;
  --dark:#1c2229;
  --dark2:#2b323a;
  --orange:#e8561b;
  --white:#ffffff;
  --text:#2a2a2a;
  --roof:#dfe1e1;
}
*{margin:0;padding:0;box-sizing:border-box}
html,body{width:1200px;height:823px;overflow:hidden;background:var(--bg)}
body{position:relative;font-family:"Montserrat",sans-serif}
.page{position:absolute;top:67px;width:520px;height:674px;background:var(--white);box-shadow:0 4px 14px rgba(0,0,0,.18);overflow:hidden}
.page--front{left:70px}
.page--back{left:622px}
.abs{position:absolute}
.header-art{position:absolute;left:0;top:0;width:520px;height:253px}
.brand{position:absolute;text-align:center;color:var(--white);font-weight:800;line-height:1}
.brand__top{font-size:28px;letter-spacing:1px}
.brand__bottom{font-size:21px;letter-spacing:1px;border-top:2px solid var(--white);padding-top:3px;margin-top:3px}
.front-title{position:absolute;left:36px;top:90px;color:var(--white);font-weight:800;line-height:1;white-space:nowrap}
.front-title__kicker{color:var(--orange);font-size:19px}
.front-title__mid{font-size:30px;margin-top:4px}
.front-title__big{font-size:58px;margin-top:-10px}
.front-intro{position:absolute;left:39px;top:206px;width:220px;font-family:"Poppins",sans-serif;font-size:10.4px;color:var(--white);line-height:1.2;white-space:nowrap}
.front-intro strong{color:var(--orange);font-weight:600}
.section-heading{position:absolute;left:38px;top:263px;color:var(--orange);font-weight:800;font-size:12.5px;white-space:nowrap}
.tile{position:absolute;width:141px;height:104px}
.tile__photo{width:141px;height:79px}
.tile__label{height:25px;display:flex;align-items:center;justify-content:center;text-align:center;color:var(--white);font-weight:700;font-size:10px;line-height:1}
.label--dark{background:var(--dark)}
.label--orange{background:var(--orange)}
.footer{position:absolute;left:0;top:630px;width:520px;height:44px}
.footer__call{position:absolute;left:38px;top:14px;color:var(--white);font-family:"Poppins",sans-serif;font-size:11.5px;display:flex;align-items:center;gap:5px;white-space:nowrap}
.footer__call b{font-family:"Montserrat",sans-serif;font-weight:700;font-size:11.5px}
.footer__links{position:absolute;left:254px;top:15px;color:var(--white);font-family:"Poppins",sans-serif;font-size:10.5px;display:flex;gap:12px;align-items:center;white-space:nowrap}
.footer__links span{display:flex;align-items:center;gap:4px}
.back-stat{position:absolute;left:282px;top:80px;width:200px;text-align:center;color:var(--white);font-weight:800;line-height:1}
.back-stat__num{color:var(--orange);font-size:72px;letter-spacing:-2px}
.back-stat__sub{color:var(--orange);font-size:10px;margin-top:4px}
.back-stat__tag{font-size:26px;margin-top:9px;line-height:.96}
.service{position:absolute;top:288px;width:84px}
.service__photo{width:84px;height:67px}
.service__label{margin-top:3px;height:25px;background:var(--orange);color:var(--white);font-weight:700;font-size:8.3px;line-height:1;display:flex;align-items:center;justify-content:center;text-align:center}
.area-bar{position:absolute;left:37px;top:389px;width:445px;height:24px;background:var(--dark);display:flex;align-items:center;color:var(--white);font-weight:800;white-space:nowrap;line-height:1}
.area-bar__title{font-size:13px;padding:0 8px 0 7px;height:24px;display:flex;align-items:center;background:var(--dark2);border-right:2px solid var(--white)}
.area-bar__text{font-size:10.8px;padding-left:8px;display:flex;align-items:center;gap:5px}
.area-bar__text em{font-style:normal;color:var(--orange)}
.about{position:absolute;top:423px;width:210px;font-family:"Poppins",sans-serif;font-size:6.6px;line-height:1.25;color:var(--text)}
.about p+p{margin-top:8px}
.cert-photo{position:absolute;left:270px;top:505px;width:250px;height:125px}
.cert-heading{top:515px}
.badge{position:absolute;background:var(--roof);border-radius:3px}
.license{position:absolute;left:36px;top:609px;display:flex;font-weight:700;font-size:7.4px;color:var(--white);line-height:1;white-space:nowrap}
.license span{padding:3px 6px;background:var(--orange);border-radius:6px 0 0 6px}
.license b{padding:3px 6px;background:var(--dark);border-radius:0 6px 6px 0}
</style>
</head>
<body>

<section class="page page--front">
  <svg class="header-art" viewBox="0 0 520 253">
    <defs>
      <linearGradient id="roofPhoto" x1="0" y1="0" x2="0" y2="1">
        <stop offset="0" stop-color="#8fb3d6"/>
        <stop offset=".32" stop-color="#b7a58a"/>
        <stop offset=".5" stop-color="#e9ebeb"/>
        <stop offset="1" stop-color="#d8dada"/>
      </linearGradient>
    </defs>
    <rect width="520" height="253" fill="var(--dark)"/>
    <polygon points="320,0 520,0 520,253 254,253" fill="url(#roofPhoto)" role="img" aria-label="Photo of a finished white membrane commercial roof with drains and parapet wall"/>
    <polygon points="316,0 323,0 257,253 250,253" fill="var(--orange)"/>
  </svg>
  <div class="brand" style="left:60px;top:27px;width:110px">
    <div class="brand__top">K&amp;R</div>
    <div class="brand__bottom">ROOFING</div>
  </div>
  <div class="front-title">
    <div class="front-title__kicker">OUR SPECIALTY IS</div>
    <div class="front-title__mid">COMMERCIAL</div>
    <div class="front-title__big">ROOFS</div>
  </div>
  <p class="front-intro">K&amp;R Roofing has been installing<br>all types of commercial roof systems<br><strong>across Arizona since 1984.</strong></p>

  <h2 class="section-heading">K&amp;R ROOFING INSTALLS THE FOLLOWING PRODUCTS:</h2>

  <div class="tile" style="left:37px;top:286px"><div class="tile__photo" role="img" aria-label="Worker welding TPO membrane seams" style="background:linear-gradient(#9a9a94,#e3e4e2 45%)"></div><div class="tile__label label--dark">TPO</div></div>
  <div class="tile" style="left:189px;top:286px"><div class="tile__photo" role="img" aria-label="White PVC roof surface" style="background:linear-gradient(#d9dfe4,#eef0ef)"></div><div class="tile__label label--orange">PVC</div></div>
  <div class="tile" style="left:341px;top:286px"><div class="tile__photo" role="img" aria-label="Modified bitumen roof" style="background:linear-gradient(#8ea7c2,#737a80 30%,#5e656a)"></div><div class="tile__label label--dark">MODIFIED BITUMEN</div></div>

  <div class="tile" style="left:37px;top:397px"><div class="tile__photo" role="img" aria-label="Silicone coating applied to a roof" style="background:linear-gradient(#c8c9c6,#e4e4e2)"></div><div class="tile__label label--orange">SILICONE COATINGS</div></div>
  <div class="tile" style="left:189px;top:397px"><div class="tile__photo" role="img" aria-label="Acrylic coated metal roof edge" style="background:linear-gradient(#5d6266,#3e4347 60%,#7b6a55)"></div><div class="tile__label label--dark">ACRYLIC COATINGS</div></div>
  <div class="tile" style="left:341px;top:397px"><div class="tile__photo" role="img" aria-label="Asphalt shingle roof" style="background:linear-gradient(#8e9094,#a7a9ab)"></div><div class="tile__label label--orange">SHINGLE</div></div>

  <div class="tile" style="left:37px;top:508px"><div class="tile__photo" role="img" aria-label="Standing seam metal roof from above" style="background:linear-gradient(135deg,#7f8890,#a9afb4)"></div><div class="tile__label label--dark">METAL</div></div>
  <div class="tile" style="left:189px;top:508px"><div class="tile__photo" role="img" aria-label="Spray foam gun applying polyurethane foam" style="background:linear-gradient(135deg,#c9653a,#8c8f92 55%,#d8572e)"></div><div class="tile__label label--orange" style="font-size:9.5px">SPRAY<br>POLYURETHANE FOAM</div></div>
  <div class="tile" style="left:341px;top:508px"><div class="tile__photo" role="img" aria-label="Orange clay tile roof" style="background:linear-gradient(160deg,#e2792f,#c95a1f)"></div><div class="tile__label label--dark">TILE AND MORE</div></div>

  <div class="footer">
    <svg class="abs" width="520" height="44" viewBox="0 0 520 44" style="left:0;top:0">
      <rect width="520" height="44" fill="var(--dark)"/>
      <polygon points="238,0 520,0 520,44 254,44" fill="var(--dark2)"/>
      <polygon points="229,0 235,0 251,44 245,44" fill="var(--white)"/>
    </svg>
    <div class="footer__call">CALL US TODAY
      <svg width="10" height="10" viewBox="0 0 24 24"><path fill="var(--orange)" d="M6.6 10.8a15.1 15.1 0 006.6 6.6l2.2-2.2c.3-.3.7-.4 1-.2 1.1.4 2.3.6 3.6.6.6 0 1 .4 1 1V20c0 .6-.4 1-1 1A17 17 0 013 4c0-.6.4-1 1-1h3.5c.6 0 1 .4 1 1 0 1.3.2 2.5.6 3.6.1.3 0 .7-.2 1z"/></svg>
      <b>555-014-2290</b></div>
    <div class="footer__links">
      <span><svg width="10" height="8" viewBox="0 0 20 16"><rect width="20" height="16" rx="2" fill="var(--orange)"/><path d="M1 2l9 7 9-7" stroke="#fff" stroke-width="2" fill="none"/></svg>info@kr-roofing.com</span>
      <span><svg width="10" height="10" viewBox="0 0 20 20"><circle cx="10" cy="10" r="8.5" fill="none" stroke="var(--orange)" stroke-width="2"/><path d="M1.5 10h17M10 1.5c-4 5-4 12 0 17M10 1.5c4 5 4 12 0 17" stroke="var(--orange)" stroke-width="1.5" fill="none"/></svg>kr-roofing.com</span>
    </div>
  </div>
</section>

<section class="page page--back">
  <svg class="header-art" viewBox="0 0 520 253">
    <defs>
      <linearGradient id="cityPhoto" x1="0" y1="0" x2="0" y2="1">
        <stop offset="0" stop-color="#a9c0d6"/>
        <stop offset=".22" stop-color="#6f7f8e"/>
        <stop offset=".35" stop-color="#9aa48f"/>
        <stop offset=".6" stop-color="#c7cbcc"/>
        <stop offset="1" stop-color="#8f9596"/>
      </linearGradient>
    </defs>
    <rect width="520" height="253" fill="var(--dark)"/>
    <polygon points="0,0 292,0 226,253 0,253" fill="url(#cityPhoto)" role="img" aria-label="Aerial photo of commercial buildings with mountains behind"/>
    <polygon points="292,0 299,0 233,253 226,253" fill="var(--orange)"/>
  </svg>
  <div class="brand" style="left:327px;top:24px;width:110px">
    <div class="brand__top">K&amp;R</div>
    <div class="brand__bottom">ROOFING</div>
  </div>
  <div class="back-stat">
    <div class="back-stat__num">40+</div>
    <div class="back-stat__sub">YEARS OF INSTALLING QUALITY</div>
    <div class="back-stat__tag">QUALITY<br>ROOFING YOU<br>CAN TRUST</div>
  </div>

  <h2 class="section-heading" style="left:36px">K&amp;R ROOFING OFFERS THE FOLLOWING SERVICES:</h2>

  <div class="service" style="left:36px"><div class="service__photo" role="img" aria-label="Crew installing a new roof" style="background:linear-gradient(#c98b5a,#3d4247)"></div><div class="service__label">New Roof<br>Installation</div></div>
  <div class="service" style="left:126px"><div class="service__photo" role="img" aria-label="Roofer re-roofing with tools" style="background:linear-gradient(#c9b79a,#d3b43c 60%,#9a7a55)"></div><div class="service__label">Re-roofing</div></div>
  <div class="service" style="left:216px"><div class="service__photo" role="img" aria-label="Worker coating a roof during maintenance" style="background:linear-gradient(#cfd5da,#e6e7e6)"></div><div class="service__label">Roof Maintenance<br>&amp; Service</div></div>
  <div class="service" style="left:306px"><div class="service__photo" role="img" aria-label="Inspector with clipboard on a roof" style="background:linear-gradient(#c3ccd4,#8c9c6a 50%,#6e7880)"></div><div class="service__label">Roof<br>Inspections</div></div>
  <div class="service" style="left:396px"><div class="service__photo" role="img" aria-label="Roof coating being applied" style="background:linear-gradient(#d2d8de,#c9cbca)"></div><div class="service__label">Roof Coatings<br>And more</div></div>

  <div class="area-bar">
    <div class="area-bar__title">SERVICE AREA</div>
    <div class="area-bar__text">
      <svg width="10" height="12" viewBox="0 0 20 24"><path d="M10 1a8 8 0 00-8 8c0 6 8 14 8 14s8-8 8-14a8 8 0 00-8-8z" fill="none" stroke="var(--orange)" stroke-width="2.4"/><circle cx="10" cy="9" r="3" fill="var(--orange)"/></svg>
      <span>WE SERVICE THE ENTIRE <em>STATE OF ARIZONA</em></span>
    </div>
  </div>

  <div class="about" style="left:37px">
    <p>K&amp;R Roofing opened the doors in 1984, and we've since installed, serviced, maintained, and coated thousands of commercial roofs around the state of Arizona, in the many climate regions of the state.</p>
    <p>Though we all live here for the constant sunshine, Arizona is one of the harshest environments in the US for roofs. Constant sun, heat, dryness, and then the torrential monsoon downpours all test the limits of your roof.</p>
  </div>
  <div class="about" style="left:270px">
    <p>We work with you to come up with a solution that works for your roof and will keep your business dry for years to come. Then, our team of project managers, superintendents, foremen, and field workers all come together to execute on that plan and install a quality roof.</p>
    <p>We are certified with many different manufacturers, so we're able to offer custom solutions to solve your issues, that will also often come with reputable manufacturer warranties.</p>
  </div>

  <div class="cert-photo" role="img" aria-label="Photo of a finished commercial building with a company service truck parked in front" style="background:linear-gradient(90deg,rgba(255,255,255,1),rgba(196,201,204,.9) 25%,#8d8f8e 60%,#b9bdbf)"></div>
  <h2 class="section-heading cert-heading" style="left:36px">CERTIFIED WITH THE FOLLOWING MANUFACTURERS:</h2>

  <div class="badge" style="left:36px;top:540px;width:90px;height:16px"></div>
  <div class="badge" style="left:140px;top:536px;width:24px;height:24px;border-radius:50%"></div>
  <div class="badge" style="left:172px;top:540px;width:78px;height:16px"></div>
  <div class="badge" style="left:36px;top:567px;width:34px;height:32px"></div>
  <div class="badge" style="left:78px;top:570px;width:76px;height:24px"></div>
  <div class="badge" style="left:162px;top:566px;width:70px;height:30px"></div>

  <div class="license"><span>CONTRACTOR LICENSE NUMBER</span><b>AZ ROC 512078</b></div>

  <div class="footer">
    <svg class="abs" width="520" height="44" viewBox="0 0 520 44" style="left:0;top:0">
      <rect width="520" height="44" fill="var(--dark)"/>
      <polygon points="238,0 520,0 520,44 254,44" fill="var(--dark2)"/>
      <polygon points="229,0 235,0 251,44 245,44" fill="var(--white)"/>
    </svg>
    <div class="footer__call">CALL US TODAY
      <svg width="10" height="10" viewBox="0 0 24 24"><path fill="var(--orange)" d="M6.6 10.8a15.1 15.1 0 006.6 6.6l2.2-2.2c.3-.3.7-.4 1-.2 1.1.4 2.3.6 3.6.6.6 0 1 .4 1 1V20c0 .6-.4 1-1 1A17 17 0 013 4c0-.6.4-1 1-1h3.5c.6 0 1 .4 1 1 0 1.3.2 2.5.6 3.6.1.3 0 .7-.2 1z"/></svg>
      <b>555-014-2290</b></div>
    <div class="footer__links">
      <span><svg width="10" height="8" viewBox="0 0 20 16"><rect width="20" height="16" rx="2" fill="var(--orange)"/><path d="M1 2l9 7 9-7" stroke="#fff" stroke-width="2" fill="none"/></svg>info@kr-roofing.com</span>
      <span><svg width="10" height="10" viewBox="0 0 20 20"><circle cx="10" cy="10" r="8.5" fill="none" stroke="var(--orange)" stroke-width="2"/><path d="M1.5 10h17M10 1.5c-4 5-4 12 0 17M10 1.5c4 5 4 12 0 17" stroke="var(--orange)" stroke-width="1.5" fill="none"/></svg>kr-roofing.com</span>
    </div>
  </div>
</section>

</body>
</html>
```